Harbourline Blinds & Shutters

It Needs to look classy as my target is the upper end of the blind market
I need a Logo design on front and description on back of what i do:
- Roller Blinds
- Vertical Blinds
- Venetian Blinds
- Plantation Shutters
- Aluminum External Shutters
and contact details
Gavin
0418527306
and
Terry
0421690358
Updates
Hi Guys,
Sorry for the no feedback but i was waiting on my logo design. But its done now i have uploaded it. so if you could take a look and send through some designs
Reason: my logo was just finished an i just uploaded it today really dont understand why my deadline has been rached foe my bizcards as it states no deadline. But please extend
Target Market(s)
People that live on the coast and are looking for classy good quality blinds and shutters
Font styles to use
Other font styles liked:
- Copperplate Gothic,open to suggestion
Look and feel
Each slider illustrates characteristics of the customer's brand and the style your logo design should communicate.

```html
<!DOCTYPE html>
<html lang="en">
<head>
<meta charset="UTF-8">
<title>Harbourline Blinds &amp; Shutters – Business Cards</title>
<link href="https://fonts.googleapis.com/css2?family=Bitter:wght@400;600&display=swap" rel="stylesheet">
<style>
  :root {
    --brand-red: #d0151b;
    --band-red: #c3141a;
    --card-white: #ffffff;
    --card-grey: #eeeeee;
    --tint-light: #f6f6f6;
    --tint-mid: #e6e6e6;
    --text-grey: #555555;
    --icon-grey: #7a7a7a;
    --backdrop: #e4e0d6;
    --shadow: rgba(0, 0, 0, 0.22);
  }
  * { box-sizing: border-box; margin: 0; padding: 0; }
  html, body {
    width: 1200px; height: 800px; overflow: hidden;
    background: var(--backdrop);
    font-family: "Bitter", Georgia, serif;
  }
  .canvas { position: relative; width: 1200px; height: 800px; }
  .card {
    position: absolute; width: 560px; height: 320px;
    background: linear-gradient(180deg, var(--card-white) 0%, var(--card-grey) 100%);
    box-shadow: 0 10px 24px var(--shadow);
    overflow: hidden;
  }
  .card--front { left: 70px; top: 70px; }
  .card--back { left: 570px; top: 410px; }

  .brand { position: absolute; display: flex; flex-direction: column; align-items: center; }
  .brand__mark {
    width: 78px; height: 78px; border-radius: 50%;
    background: var(--brand-red); margin-bottom: 12px;
  }
  .brand__name {
    color: var(--brand-red); font-weight: 400; text-align: center;
    line-height: 1.05; text-transform: uppercase;
  }
  .brand__name span { display: block; }
  .card--front .brand { left: 26px; top: 98px; width: 220px; }
  .card--front .brand__name { font-size: 26px; }
  .card--front .brand__name .brand__sub { font-size: 11px; letter-spacing: 1px; margin-top: 4px; }

  .contact { position: absolute; left: 270px; color: var(--text-grey); font-size: 14px; }
  .contact__name { font-size: 17px; margin-bottom: 3px; }
  .contact__line { display: flex; align-items: center; gap: 8px; line-height: 1.45; }
  .contact__line svg { width: 14px; height: 14px; fill: none; stroke: var(--icon-grey); stroke-width: 1.6; }
  .contact--first { top: 22px; }
  .contact--second { top: 222px; }

  .services {
    position: absolute; left: 254px; top: 102px; right: 0; height: 108px;
    background: var(--band-red); color: var(--card-white);
    list-style: none; padding: 14px 18px; font-size: 13.5px; line-height: 1.35;
  }
  .services li::before { content: "- "; }

  .back-tint {
    position: absolute; inset: 0;
    background: linear-gradient(160deg, var(--card-white) 0%, var(--tint-light) 45%, var(--tint-mid) 100%);
  }
  .card--back .brand { left: 0; right: 0; top: 78px; }
  .card--back .brand__name { font-size: 34px; }
  .card--back .brand__name .brand__sub { font-size: 13px; letter-spacing: 1.5px; margin-top: 4px; }
</style>
</head>
<body>
<main class="canvas">
  <section class="card card--front" aria-label="Business card, contact side">
    <div class="brand">
      <div class="brand__mark"></div>
      <p class="brand__name"><span>Harbourline</span><span class="brand__sub">Blinds &amp; Shutters</span></p>
    </div>

    <div class="contact contact--first">
      <p class="contact__name">Gavin</p>
      <p class="contact__line"><svg viewBox="0 0 16 16"><path d="M4 2l2.5 3-1.5 1.5a8 8 0 0 0 4.5 4.5L11 9.5l3 2.5-1.5 2A10 10 0 0 1 2 3.5z"/></svg>0418527306</p>
      <p class="contact__line"><svg viewBox="0 0 16 16"><rect x="1.5" y="3.5" width="13" height="9"/><path d="M1.5 3.5L8 9l6.5-5.5"/></svg>gavin@harbourmail.com</p>
    </div>

    <ul class="services">
      <li>Roller Blinds</li>
      <li>Vertical Blinds</li>
      <li>Venetian Blinds</li>
      <li>Plantation Shutters</li>
      <li>Aluminum External Shutters</li>
    </ul>

    <div class="contact contact--second">
      <p class="contact__name">Terry</p>
      <p class="contact__line"><svg viewBox="0 0 16 16"><path d="M4 2l2.5 3-1.5 1.5a8 8 0 0 0 4.5 4.5L11 9.5l3 2.5-1.5 2A10 10 0 0 1 2 3.5z"/></svg>0421690358</p>
      <p class="contact__line"><svg viewBox="0 0 16 16"><rect x="1.5" y="3.5" width="13" height="9"/><path d="M1.5 3.5L8 9l6.5-5.5"/></svg>terry@harbourmail.com</p>
    </div>
  </section>

  <section class="card card--back" aria-label="Business card, brand side">
    <div class="back-tint" role="img" aria-label="Faint light grey brand decoration across the card background"></div>
    <div class="brand">
      <div class="brand__mark"></div>
      <p class="brand__name"><span>Harbourline</span><span class="brand__sub">Blinds &amp; Shutters</span></p>
    </div>
  </section>
</main>
</body>
</html>
```